NEW Gym Timetable for Muay Thai gym!

We need a new timetable for our Muay Thai gym - the times, classes and logos are attached. Our primary logo font is MACHINE BT

The gym is called Kalto Vex. The address is Level 2, 218-220 Brannock Road, Pellwood, Canberra

We are open Monday to Saturday and Sunday by appointment.

Our website and more information can be found at www.kaltovex.com.au.

Please message me for more information/feedback

```html
<!DOCTYPE html>
<html lang="en">
<head>
<meta charset="utf-8">
<title>Kalto Vex — Class Timetable</title>
<link rel="stylesheet" href="https://fonts.googleapis.com/css2?family=Alfa+Slab+One&family=Archivo+Black&family=Roboto+Condensed:wght@400;700&display=swap">
<style>
  :root {
    --green: #0f7a3f;
    --green-bright: #128a47;
    --green-ink: #10743c;
    --green-deep: #0d2a19;
    --footer: #0c2416;
    --stripe: #e2e3e1;
    --paper: #ffffff;
    --rule: #d4d5d3;
    --ghost: #b9c7bb;
  }
  html, body { margin: 0; padding: 0; overflow: hidden; }
  body { width: 928px; height: 1200px; position: relative; background: var(--paper); font-family: "Roboto Condensed", "Arial Narrow", sans-serif; }

  .masthead {
    position: absolute; left: 0; top: 0; width: 928px; height: 348px;
    background: linear-gradient(180deg, #ffffff 0%, #f4f4f4 25%, #d2d2d2 100%);
  }
  .masthead__band {
    position: absolute; left: 0; top: 352px; width: 928px; height: 68px;
    background: var(--green);
  }
  .brand {
    position: absolute; left: 0; top: 118px; width: 928px; text-align: center;
    font-family: "Roboto Condensed", "Arial Narrow", sans-serif; font-weight: 700;
    font-size: 120px; letter-spacing: 6px; color: var(--green); line-height: 1;
    text-transform: uppercase;
  }

  .timetable {
    position: absolute; left: 0; top: 426px; width: 928px;
    display: grid;
    grid-template-columns: 142px 196px 196px 198px 196px;
    grid-template-rows: 124px 108px 96px 101px 100px 100px 84px;
  }
  .day {
    display: flex; align-items: center; justify-content: center;
    font-family: "Alfa Slab One", Georgia, serif; color: #fff; font-size: 42px;
    border-bottom: 1px solid rgba(255,255,255,0.08);
  }
  .day small { font-size: 31px; }
  .day--mo { background: #128a47; }
  .day--tu { background: #0f6f3a; }
  .day--we { background: #0e6133; }
  .day--th { background: #0d542d; }
  .day--fr { background: #0d4627; }
  .day--sa { background: #0d3821; }
  .day--su { background: var(--green-deep); }

  .slot {
    text-align: center; color: var(--green-ink);
    border-bottom: 1px solid var(--rule);
    padding-top: 18px; box-sizing: border-box;
  }
  .slot--shade { background: var(--stripe); }
  .slot__time { font-size: 19px; font-weight: 400; line-height: 26px; }
  .slot__time .mer { font-size: 14px; }
  .slot__class { font-size: 18.5px; font-weight: 700; line-height: 27px; text-transform: uppercase; }
  .slot__note { font-size: 12.5px; line-height: 20px; text-transform: uppercase; }
  .slot--mid { display: flex; flex-direction: column; justify-content: center; padding-top: 0; }
  .slot--mark { display: flex; align-items: center; justify-content: center; padding-top: 0; }
  .mark { width: 56px; height: 68px; background: var(--ghost); }

  .appointment {
    position: absolute; left: 142px; top: 1075px; width: 786px; height: 64px;
    display: flex; align-items: center; justify-content: center;
    font-family: "Archivo Black", "Arial Black", sans-serif; font-style: italic;
    color: var(--green-ink); font-size: 36px; letter-spacing: 0.5px; white-space: nowrap;
  }
  .appointment .lite { font-size: 27px; }

  .footer {
    position: absolute; left: 0; top: 1139px; width: 928px; height: 61px;
    background: var(--footer);
    display: flex; align-items: center; justify-content: center;
    font-family: "Archivo Black", "Arial Black", sans-serif; font-style: italic;
    font-size: 27px; color: var(--green-bright); letter-spacing: 1px;
  }
</style>
</head>
<body>
  <header class="masthead"></header>
  <div class="masthead__band"></div>
  <div class="brand">Kalto Vex</div>

  <main class="timetable">
    <div class="day day--mo">M<small>O</small></div>
    <div class="slot slot--shade"><div class="slot__time">6:00<span class="mer">AM</span> - 7:00<span class="mer">AM</span></div><div class="slot__class">Clinching</div><div class="slot__note">(Fighters/by invitation)</div></div>
    <div class="slot"><div class="slot__time">5:30<span class="mer">PM</span> - 6:30<span class="mer">PM</span></div><div class="slot__class">Muay Thai</div></div>
    <div class="slot slot--shade"><div class="slot__time">6:30<span class="mer">PM</span> - 7:30<span class="mer">PM</span></div><div class="slot__class">Padwork &amp;<br>Bagwork</div></div>
    <div class="slot"><div class="slot__time">7:30<span class="mer">PM</span> - 8:30<span class="mer">PM</span></div><div class="slot__class">Fighters</div></div>

    <div class="day day--tu">T<small>U</small></div>
    <div class="slot slot--shade"><div class="slot__time">6:00<span class="mer">AM</span> - 7:00<span class="mer">AM</span></div><div class="slot__class">Muay HIIT</div></div>
    <div class="slot"><div class="slot__time">5:30<span class="mer">PM</span> - 6:30<span class="mer">PM</span></div><div class="slot__class">Boxing</div></div>
    <div class="slot slot--shade"><div class="slot__time">6:30<span class="mer">PM</span> - 7:30<span class="mer">PM</span></div><div class="slot__class">Muay HIIT</div></div>
    <div class="slot"><div class="slot__time">7:30<span class="mer">PM</span> - 8:30<span class="mer">PM</span></div><div class="slot__class">Fighters</div></div>

    <div class="day day--we">W<small>E</small></div>
    <div class="slot slot--shade"><div class="slot__time">6:00<span class="mer">AM</span> - 7:00<span class="mer">AM</span></div><div class="slot__class">Clinching</div><div class="slot__note">(Fighters/by invitation)</div></div>
    <div class="slot"><div class="slot__time">5:30<span class="mer">PM</span> - 6:30<span class="mer">PM</span></div><div class="slot__class">Muay Thai</div></div>
    <div class="slot slot--shade"><div class="slot__time">6:30<span class="mer">PM</span> - 7:30<span class="mer">PM</span></div><div class="slot__class">Padwork &amp;<br>Bagwork</div></div>
    <div class="slot"><div class="slot__time">7:30<span class="mer">PM</span> - 8:30<span class="mer">PM</span></div><div class="slot__class">Fighters</div></div>

    <div class="day day--th">T<small>H</small></div>
    <div class="slot slot--shade"><div class="slot__time">6:00<span class="mer">AM</span> - 7:00<span class="mer">AM</span></div><div class="slot__class">Muay HIIT</div></div>
    <div class="slot"><div class="slot__time">5:30<span class="mer">PM</span> - 6:30<span class="mer">PM</span></div><div class="slot__class">Boxing</div></div>
    <div class="slot slot--shade"><div class="slot__time">6:30<span class="mer">PM</span> - 7:30<span class="mer">PM</span></div><div class="slot__class">Muay HIIT</div></div>
    <div class="slot"><div class="slot__time">7:30<span class="mer">PM</span> - 8:30<span class="mer">PM</span></div><div class="slot__class">Fighters</div></div>

    <div class="day day--fr">F<small>R</small></div>
    <div class="slot slot--shade slot--mark"><div class="mark"></div></div>
    <div class="slot slot--mid"><div class="slot__class">Muay HIIT<br>Weekly Wrap</div></div>
    <div class="slot slot--shade slot--mark"><div class="mark"></div></div>
    <div class="slot slot--mark"><div class="mark"></div></div>

    <div class="day day--sa">S<small>A</small></div>
    <div class="slot slot--shade"><div class="slot__time">8:00<span class="mer">AM</span> - 8:45<span class="mer">AM</span></div><div class="slot__class">Muay HIIT</div></div>
    <div class="slot"><div class="slot__time">9:00<span class="mer">PM</span> - 11:00<span class="mer">PM</span></div><div class="slot__class">Sparring</div></div>
    <div class="slot slot--shade"><div class="slot__time">12:00<span class="mer">PM</span> - 1:00<span class="mer">PM</span></div><div class="slot__class">Muay HIIT</div></div>
    <div class="slot slot--mark"><div class="mark"></div></div>

    <div class="day day--su">S<small>U</small></div>
    <div class="slot slot--shade"></div>
    <div class="slot"></div>
    <div class="slot slot--shade"></div>
    <div class="slot"></div>
  </main>

  <div class="appointment">PERSONAL TRAINING&nbsp;<span class="lite">BY APPOINTMENT</span></div>

  <footer class="footer">FOR MORE INFO CONTACT US</footer>
</body>
</html>
```